Pet Sitting Business Card

Would like a business card designed for my new pet sitting business
Card needs to match with logo design.
Blue and Orange are the theme colours.

Simple yet sophisticated design

company name:- MARIGOLD PET CARE
Tessa Brundle
Owner
0462157093
tessa@marigoldpetcare.com.au
www.marigoldpetcare.com.au

I'm going to close my deadline early. I will be picking a winner by the 10th of May. Please submit designs before then.
thank you

Target Market(s)

All types of professional pet lovers wishing to have their pet looked after

Industry/Entity Type

Pet

Requirements
Must have
• Logo design
Blue and orange

```html
<!DOCTYPE html>
<html lang="en">
<head>
<meta charset="utf-8">
<title>Marigold Pet Care – Business Card</title>
<link rel="stylesheet" href="https://fonts.googleapis.com/css2?family=Libre+Baskerville:ital,wght@0,400;0,700;1,400;1,700&display=swap">
<style>
  :root {
    --page-bg: #e9e9ea;
    --card-white: #ffffff;
    --peach-top: #fcc38c;
    --peach-bottom: #fde8d6;
    --brand-blue: #1e8ff0;
    --brand-orange: #ea8a2e;
    --card-shadow: rgba(0, 0, 0, 0.18);
  }
  * { box-sizing: border-box; margin: 0; padding: 0; }
  html, body {
    width: 1200px;
    height: 848px;
    overflow: hidden;
    background: var(--page-bg);
    font-family: "Libre Baskerville", Georgia, serif;
  }
  .stage {
    position: relative;
    width: 1200px;
    height: 848px;
  }
  .card {
    position: absolute;
    top: 284px;
    width: 530px;
    height: 280px;
    overflow: hidden;
    background: linear-gradient(180deg, var(--peach-top), var(--peach-bottom));
    box-shadow: 0 3px 10px var(--card-shadow);
  }
  .card--front { left: 50px; }
  .card--back { left: 620px; }
  .card__oval {
    position: absolute;
    left: -3%;
    top: -14%;
    width: 106%;
    height: 128%;
    border-radius: 50%;
    background: var(--card-white);
  }
  .brand {
    position: absolute;
    display: flex;
    flex-direction: column;
    align-items: center;
    text-align: center;
  }
  .brand__dot {
    width: 34px;
    height: 34px;
    border-radius: 50%;
    background: var(--brand-orange);
    margin-bottom: 12px;
  }
  .brand__name {
    color: var(--brand-blue);
    font-weight: 700;
    letter-spacing: 0.04em;
    line-height: 1.15;
  }
  .card--front .brand {
    left: 0;
    right: 0;
    top: 78px;
  }
  .card--front .brand__name { font-size: 26px; }
  .card--back .brand {
    left: 40px;
    width: 140px;
    top: 96px;
  }
  .card--back .brand__dot { width: 22px; height: 22px; margin-bottom: 8px; }
  .card--back .brand__name { font-size: 15px; }
  .person {
    position: absolute;
    left: 242px;
    top: 68px;
  }
  .person__name {
    color: var(--brand-blue);
    font-style: italic;
    font-weight: 700;
    font-size: 24px;
    line-height: 1.1;
  }
  .person__role {
    color: var(--brand-orange);
    font-style: italic;
    font-size: 17px;
    margin-top: 4px;
  }
  .contact {
    position: absolute;
    left: 242px;
    top: 160px;
    list-style: none;
    color: var(--brand-orange);
    font-size: 15px;
    line-height: 20px;
  }
  .contact__item { display: flex; align-items: center; white-space: nowrap; }
  .contact__icon { width: 16px; height: 14px; margin-right: 7px; fill: var(--brand-orange); }
</style>
</head>
<body>
<main class="stage">
  <section class="card card--front" aria-label="Business card front">
    <div class="card__oval"></div>
    <div class="brand">
      <span class="brand__dot"></span>
      <span class="brand__name">MARIGOLD<br>PET CARE</span>
    </div>
  </section>

  <section class="card card--back" aria-label="Business card back">
    <div class="card__oval"></div>
    <div class="brand">
      <span class="brand__dot"></span>
      <span class="brand__name">MARIGOLD<br>PET CARE</span>
    </div>
    <div class="person">
      <p class="person__name">Tessa Brundle</p>
      <p class="person__role">Owner</p>
    </div>
    <ul class="contact">
      <li class="contact__item">
        <svg class="contact__icon" viewBox="0 0 16 14" aria-hidden="true">
          <path d="M1 4c0-2 3-3 7-3s7 1 7 3v1h-3.5V3.5h-7V5H1z"/>
          <path d="M4 6h8l2 7H2z"/>
        </svg>
        0462157093
      </li>
      <li class="contact__item">tessa@marigoldpetcare.com.au</li>
      <li class="contact__item">www.marigoldpetcare.com.au</li>
    </ul>
  </section>
</main>
</body>
</html>
```